Digital Product Store Front for Educational Leaders (PraisewithPenelope)

I am an a Principal, Author and Education consultant I am in need of a wordpress website that fits my brand that I will be able to sell digital products I have created, digital courses I have created, and offer mentorship and coaching services. I have my branding documents and my content/wording in the files. This website should be professional yet relatable. I'd like it to be clean, easy to navigate and be very obvious with its purpose. Please view the attached documents to give a much clearer idea about my brand and wants. :)

Target Market(s)

Educational Leaders (Principals)

Industry/Entity Type

Educational Leadership

Coding

Coded - Design and coding required

Number of Pages Required

1 page

Font styles to use
Other font styles liked:
• please use my branding font

Requirements
Must have
• All the items I listed on my document, my brand colors and font, The content I submitted is still in a very draft format but just to give the designer and idea.

```html
<!DOCTYPE html>
<html lang="en">
<head>
<meta charset="utf-8">
<title>PraisewithPenelope — Educational Leadership</title>
<link href="https://fonts.googleapis.com/css2?family=Didact+Gothic&family=Montserrat:wght@400;500;600&display=swap" rel="stylesheet">
<style>
:root{
  --teal:#5b9e91;
  --teal-dark:#4e8f83;
  --teal-light:#a8cec6;
  --cream:#f4efe3;
  --sand:#e8dcc3;
  --ink:#333333;
  --muted:#666666;
  --white:#ffffff;
  --line:#d8d8d8;
}
*{box-sizing:border-box;margin:0;padding:0}
html,body{width:1200px;height:3454px;overflow:hidden}
body{position:relative;background:var(--white);font-family:"Montserrat",sans-serif;color:var(--ink)}
.abs{position:absolute}
.heading{font-family:"Didact Gothic",sans-serif;font-weight:400;color:var(--teal);letter-spacing:1px}
.btn{position:absolute;display:flex;align-items:center;justify-content:center;background:var(--teal);color:var(--white);font-size:15px;font-weight:500;letter-spacing:.5px;text-transform:uppercase}
.brand{font-family:"Montserrat",sans-serif;font-weight:600;color:var(--teal);font-size:17px;letter-spacing:.3px}

/* nav */
.nav{position:absolute;top:0;left:0;width:1200px;height:76px;background:var(--white)}
.nav .brand{position:absolute;left:107px;top:27px}
.nav-links{position:absolute;left:325px;top:29px;display:flex}
.nav-links span{font-size:15px;font-weight:500;margin-right:58px}
.nav .contact{left:902px;top:17px;width:157px;height:45px;background:var(--teal-light);font-size:15px}

/* hero */
.hero{position:absolute;top:76px;left:0;width:1200px;height:591px;background:linear-gradient(90deg,#f6f4f3 0%,#f3f1f0 100%)}
.hero-photo{position:absolute;left:520px;top:0;width:680px;height:591px;background:linear-gradient(120deg,#f3f1f0 0%,#d8c7bb 35%,#e9c3b2 65%,#f1efee 100%)}
.hero h1{position:absolute;left:117px;top:148px;font-size:43px;line-height:48px;font-family:"Didact Gothic",sans-serif;font-weight:400;color:var(--teal);letter-spacing:1.5px}
.hero p{position:absolute;left:120px;top:253px;width:430px;font-size:16px;line-height:30px}
.hero .btn{left:122px;top:362px;width:176px;height:49px}

/* services */
.card{position:absolute;top:762px;width:314px;height:322px;border:1px solid var(--teal-light);background:var(--white);text-align:center}
.card.featured{background:linear-gradient(160deg,var(--teal) 0%,var(--teal-light) 100%);border:none;box-shadow:0 10px 30px rgba(91,158,145,.35);color:var(--white)}
.card .icon{position:absolute;left:99px;top:-57px;width:114px;height:114px;border-radius:50%;background:var(--cream);border:4px solid var(--teal-light)}
.card h3{margin-top:86px;font-size:22px;font-family:"Didact Gothic",sans-serif;font-weight:400;color:var(--teal);letter-spacing:1px}
.card.featured h3{color:var(--white)}
.card p{margin:18px auto 0;width:262px;font-size:12.5px;line-height:21.5px;color:var(--muted)}
.card.featured p{color:var(--white)}
.card .btn{left:84px;top:247px;width:146px;height:41px;font-size:15px}
.card.featured .btn{background:var(--cream);color:var(--teal)}

/* book */
.book{position:absolute;top:1167px;left:0;width:1200px;height:710px;background:linear-gradient(180deg,var(--cream) 0%,#f2ecdd 70%,var(--sand) 100%)}
.book-circle{position:absolute;left:141px;top:1502px;width:180px;height:180px;border-radius:50%;background:var(--teal-light)}
.book-cover{position:absolute;left:197px;top:1251px;width:268px;height:402px;background:linear-gradient(180deg,#f4f1ec 0%,#e6dbcd 55%,#f2efea 100%);box-shadow:8px 8px 0 #fff}
.book h2{position:absolute;left:613px;top:150px;font-size:43px}
.book h2::after{content:"";display:inline-block;width:50px;height:2px;background:var(--teal);margin-left:8px;vertical-align:middle}
.book p{position:absolute;left:613px;top:210px;width:480px;font-size:16px;line-height:30px}
.book .btn{left:614px;top:387px;width:176px;height:48px;font-size:16px}

/* newsletter */
.news{position:absolute;left:109px;top:1757px;width:984px;height:194px;background:linear-gradient(100deg,var(--teal) 0%,var(--teal) 40%,var(--teal-light) 100%);box-shadow:0 8px 22px rgba(0,0,0,.1)}
.news h4{position:absolute;left:59px;top:50px;width:420px;font-size:22px;line-height:34px;font-weight:400;color:var(--white);font-family:"Didact Gothic",sans-serif;text-transform:uppercase;letter-spacing:.2px}
.news small{position:absolute;left:60px;top:124px;font-size:14px;color:var(--white)}
.news .field{position:absolute;left:494px;top:64px;width:444px;height:54px;background:var(--white)}
.news .field span{position:absolute;left:28px;top:19px;font-size:12.5px;color:var(--muted)}
.news .field .btn{left:308px;top:6px;width:129px;height:41px;font-size:12px;font-weight:600}

/* meet */
.meet h2{position:absolute;left:130px;top:2082px;font-size:48px}
.meet h2::after{content:"";display:inline-block;width:56px;height:2px;background:var(--teal);margin-left:20px;vertical-align:middle}
.meet-copy{position:absolute;left:130px;top:2162px;width:510px;font-size:16px;line-height:26px}
.meet-copy p+p{margin-top:26px}
.meet .btn{left:130px;top:2471px;width:186px;height:50px;font-size:16px}
.meet-block{position:absolute;left:746px;top:2226px;width:378px;height:322px;background:var(--teal-light)}
.meet-photo{position:absolute;left:680px;top:2052px;width:421px;height:474px;background:linear-gradient(180deg,#eeecea 0%,#e9e4df 60%,#dcd6d0 100%)}

/* message */
.message{position:absolute;top:2673px;left:0;width:1200px;height:572px;background:var(--teal);color:var(--white)}
.ring{position:absolute;left:102px;top:80px;width:408px;height:408px;border-radius:50%;border:1.5px solid rgba(255,255,255,.6)}
.portrait{position:absolute;left:128px;top:106px;width:356px;height:356px;border-radius:50%;background:linear-gradient(160deg,#f3f1ef 0%,#e5d9cf 60%,#f0ece8 100%)}
.message h2{position:absolute;left:543px;top:88px;font-size:38px;color:var(--white);font-family:"Didact Gothic",sans-serif;font-weight:400;letter-spacing:1px}
.message .copy{position:absolute;left:544px;top:148px;width:570px;font-size:13.5px;line-height:24px}
.message .copy .gap{margin-top:24px}

/* footer */
.footer .brand{position:absolute;left:140px;top:3292px;font-size:18px}
.foot-links{position:absolute;left:373px;top:3293px;display:flex}
.foot-links span{font-size:15px;font-weight:500;margin-right:60px;letter-spacing:.4px}
.foot-line{position:absolute;left:0;top:3359px;width:1200px;height:1px;background:var(--line)}
.copyright{position:absolute;left:140px;top:3391px;font-size:12px;color:var(--muted)}
.social{position:absolute;top:3373px;width:40px;height:40px;border-radius:50%;background:#f1ebdd}
.social.on{background:var(--teal)}
</style>
</head>
<body>

<header class="nav">
  <div class="brand">PraisewithPenelope</div>
  <nav class="nav-links"><span>SHOP</span><span>LEARN</span><span>PARTNER</span><span>BOOK</span><span>MEET ME</span></nav>
  <div class="btn contact">Contact Me</div>
</header>

<section class="hero">
  <div class="hero-photo" role="img" aria-label="Photo of the educator smiling at a desk with a laptop, glasses and a palm plant"></div>
  <h1>YOUR SCHOOL CAN<br>ABSOLUTELY THRIVE.</h1>
  <p>Let's partner together to revolutionize your school's culture Into an engaged, high-performing community where everyone belongs.</p>
  <div class="btn">Why Wait?</div>
  <svg class="abs" style="left:312px;top:358px" width="160" height="50" viewBox="0 0 160 50" fill="none" stroke="#5b9e91" stroke-width="1.6"><path d="M4 26 C40 10 70 30 100 36 C120 40 135 30 150 12" stroke-dasharray="5 4"/><path d="M140 10 L154 6 L150 20 Z" fill="#5b9e91" stroke="none"/></svg>
</section>

<section class="services">
  <div class="card" style="left:103px">
    <div class="icon" role="img" aria-label="Digital tools icon"></div>
    <h3>DIGITAL TOOLS</h3>
    <p>From staff and student events, to ___ these digital tools are just one File. Print. away from revolutionalizing your school culture. (Printed in color of course) (Get that color ink ready!)</p>
    <div class="btn">Shop</div>
  </div>
  <div class="card featured" style="left:444px">
    <div class="icon" role="img" aria-label="Online courses icon"></div>
    <h3>INNOVATICE COURSES</h3>
    <p>From staff and student events, to ___ these digital tools are just one File. Print. away from revolutionalizing your school culture. (Printed in color of course) (Get that color ink ready!)</p>
    <div class="btn">Learn</div>
  </div>
  <div class="card" style="left:784px">
    <div class="icon" role="img" aria-label="Coaching icon"></div>
    <h3 style="margin-top:90px">AUTHENTIC COACHING</h3>
    <p>Unleash your leadership potential in this mentorship experience as we work together to curate a personalized plan to (Let's Be Smart Friends!)</p>
    <div class="btn" style="top:251px">Partner</div>
  </div>
</section>

<section class="book">
  <h2 class="heading">SHOP BOOK</h2>
  <p>The most important tool to connect your community and create a high-performing, thriving culture is YOU! Start by unleashing a people-centered leadership style and learn all the #1 Rules to create the culture you dream about by reading an Shopwell #1 <strong>New Release Culture Comes First.</strong></p>
  <div class="btn">Buy Now</div>
</section>
<div class="book-circle"></div>
<div class="book-cover" role="img" aria-label="Book cover of Culture Comes First by Penelope Hartwell with author photo"></div>
<svg class="abs" style="left:488px;top:1608px" width="160" height="50" viewBox="0 0 160 50" fill="none" stroke="#5b9e91" stroke-width="1.6"><path d="M156 8 C120 6 100 20 80 34 C60 46 40 44 18 36" stroke-dasharray="5 4"/><path d="M4 30 L20 28 L14 42 Z" fill="#5b9e91" stroke="none"/></svg>

<section class="news">
  <h4>Sign-up for the<br>PraisewithPenelope Newsletter</h4>
  <small>Who doesn't want more emails?</small>
  <div class="field"><span>Your Email address</span><div class="btn">Subscribe</div></div>
</section>

<section class="meet">
  <h2 class="heading">MEET ME</h2>
  <div class="meet-copy">
    <p>(Why, hello there!) Welcome to PraisewithPenelope! I am Penelope Hartwell an Elementary Principal in Maple Falls, Oregon, Author of Culture Comes First, and Education Consultant. I am super passionate about bringing change to the way school leaders serve –both children and adults.</p>
    <p>I was a teacher for eight years, and then an instructional coach, before earning my dream job as an elementary school principal! I am now in my sixth year as a school leader and have dramatically shifted the traditional elementary school culture into a thriving, loving community</p>
  </div>
  <div class="btn">Contact Me</div>
  <svg class="abs" style="left:490px;top:2470px" width="160" height="50" viewBox="0 0 160 50" fill="none" stroke="#5b9e91" stroke-width="1.6"><path d="M156 6 C120 4 100 20 80 32 C60 44 40 42 18 34" stroke-dasharray="5 4"/><path d="M4 26 L20 24 L14 38 Z" fill="#5b9e91" stroke="none"/></svg>
  <div class="meet-block"></div>
  <div class="meet-photo" role="img" aria-label="Portrait of the educator in glasses holding a notebook and pen"></div>
</section>

<section class="message">
  <div class="ring"></div>
  <div class="portrait" role="img" aria-label="Round portrait of the educator in a cream sweater"></div>
  <h2>A MESSAGE FROM ME</h2>
  <div class="copy">
    <p>I am so happy you are here! (Seriously!) Working with other educational leaders brings me THE. MOST. JOY. (I'm OBSESSED)</p>
    <p class="gap">I want to support you on every inch of your journey! We can work alongside each other to navigate the challenges of leading adults, transforming student behaviors, and creating a vibrant atmosphere.</p>
    <p>School leadership can be lonely, taxing, and overwhelming. Often, the biggest challenge is knowing where to start as you face the pressures and demands from the many stakeholders.</p>
    <p>But don't worry, I can't wait to help you! So whether you need tools to enhance your own leadership skills, to facilitate connection within your community, or to transform student behaviors, I am here to help you develop your school into a high-performing culture. Let's get started today!!</p>
  </div>
</section>

<footer class="footer">
  <div class="brand">PraisewithPenelope</div>
  <nav class="foot-links"><span>SHOP</span><span>LEARN</span><span>PARTNER</span><span>BOOK</span><span>MEET ME</span><span>CONTACT ME</span></nav>
  <div class="foot-line"></div>
  <div class="copyright">© 2024 PraisewithPenelope. All Rights Reserved</div>
  <div class="social" style="left:931px" aria-label="Social link"></div>
  <div class="social on" style="left:977px" aria-label="Social link"></div>
  <div class="social" style="left:1025px" aria-label="Social link"></div>
</footer>

</body>
</html>
```